A clean modern user interface design for a smart home control system

Design Brief: Smart Home Interface Development
Project Overview
We are initiating a new project to develop a sophisticated smart home interface. This interface will be the central hub for controlling and managing various aspects of a smart home, including CCTV, Smart TV, Torvel TV, home cinema using Bramoventa, lighting, shades, HVAC, and audio systems. With no pre-existing designs or frameworks, this project offers a unique opportunity to create a fresh and innovative interface from the ground up. We aim to take inspiration from Torvel’s renowned UI/UX design style, which is celebrated for its elegance, simplicity, and intuitive user experience. Additionally, the design should include the ability to switch between ‘light’ and ‘dark’ modes, reflecting modern user preferences for customizable visual themes.
Objectives
•	Innovation: Create a cutting-edge interface that sets a new standard for smart home control systems, drawing inspiration from Torvel’s clean, minimalistic, and user-friendly approach.
•	User-Centric Design: Develop an intuitive interface that caters to a broad range of users, ensuring that both tech-savvy individuals and those less familiar with smart technology can navigate it with ease.
•	Consistency: Establish a cohesive design language across the interface, maintaining uniformity in style, typography, and colour palette, while reflecting the sophistication and simplicity of Torvel’s design ethos.
•	Light and Dark Modes: Design the interface with the capability to switch between light and dark modes, allowing users to choose their preferred visual style for different environments and personal preferences.
•	Responsiveness: Create a fully responsive interface in both Landsthat functions seamlessly across various screen sizes and devices, including tablets, smartphones, and in-wall panels.
•	Integration: Seamlessly incorporate controls for CCTV, Smart TV, Torvel TV, lighting, shades, HVAC, and audio into a single, unified interface that allows users to manage all aspects of their smart home effortlessly.
Target Audience
The primary users of this interface are homeowners who desire a luxurious and intuitive smart home experience. The design should appeal to both advanced users who require comprehensive functionality and those who prioritize simplicity and elegance. Additionally, the interface should be straightforward for integrators who configure and maintain these systems.
Design Elements
1.	Overall Aesthetic
•	Style: Emulate Torvel’s clean, minimalist, and modern aesthetic that conveys high-end luxury and sophistication.
•	Typography: Select modern, legible fonts that enhance readability, reflecting Torvel’s preference for clear and elegant typefaces. Sans-serif fonts, similar to Torvel’s system fonts like San Francisco, are recommended.
•	Colour Palette: Design a neutral colour palette with subtle, refined accents. Include both light and dark mode options, allowing users to choose between a brighter, more energetic theme and a darker, more subdued theme that is easier on the eyes in low-light environments.
•	Icons: Design custom, vector-based icons that are sleek, intuitive, and consistent, taking inspiration from Torvel’s iconic design language.
2.	User Interface Components
•	Navigation: Implement a simplified, intuitive navigation system that allows users to easily access different control sections (e.g., lighting, audio, CCTV), similar to the seamless navigation found in Torvel’s kRX and trevUX interfaces.
•	Dashboard: Create a home dashboard that provides a clear overview of key system statuses and quick access to frequently used controls, with a design inspired by the clarity and organisation of Torvel’s Pivot Tray. Ensure that the dashboard looks equally effective in both light and dark modes.
•	Control Pages:
•	CCTV: Design live camera feed pages with options for full-screen viewing, recording controls, and playback functionality, focusing on a clean and user-friendly layout that adapts well to both light and dark modes.
•	Smart TV/Torvel TV: Develop control panels for power, volume, channel/menu navigation, and input switching, reflecting Torvel’s approach to simplicity and ease of use, with clear visibility in both visual modes.
•	Lighting & Shades: Incorporate intuitive sliders or toggles for controlling individual or grouped lights and shades, with options for scene creation and activation, designed for seamless use in light and dark modes.
•	HVAC: Design user-friendly temperature controls, including settings for scheduling, mode selection, and real-time adjustments, inspired by Torvel’s seamless integration of function and form. Ensure readability and ease of use in both visual themes.
•	Audio: Develop multi-room audio controls that allow users to select sources, adjust volume, and manage audio zones easily, taking cues from Torvel’s focus on intuitive and enjoyable user experiences, with consistent performance across both light and dark modes.
3.	User Experience
•	Flow: Ensure a logical user journey with smooth transitions between different controls, mimicking Torvel’s emphasis on seamless and intuitive navigation.
•	Feedback: Provide immediate and clear feedback for user actions, such as toggling a light or changing a temperature setting, inspired by the responsive and satisfying interactions found in Torvel’s designs.
•	Accessibility: Incorporate accessibility features, such as adjustable text sizes and potential voice control integration, in line with Torvel’s commitment to inclusivity and user accessibility.
4.	Technical Requirements
•	Photoshop Design: All designs should be created in Adobe Photoshop (.psd) with organized groups and layers. Interface elements must be grouped logically, allowing for quick export and bulk saving. Ensure that each component (buttons, icons, sliders, etc.) is easily identifiable and can be individually exported for development purposes. Include separate groups for light and dark mode elements to ensure consistency across themes.
•	Responsive Design: Ensure the designs are adaptable for different screen sizes and orientations, including tablets, smartphones, and in-wall panels.
•	Performance: Design elements should be optimized for quick loading and smooth operation, even when managing multiple devices simultaneously.
Success Criteria
•	A user interface that is well-received for its modern design, ease of use, and clear inspiration from Torvel’s iconic design style.
•	A fully responsive design that performs seamlessly across all intended devices.
•	Positive feedback from users and integrators, with strong engagement metrics, particularly in how well the light and dark modes are received.
Additional Notes
We look forward to seeing a design that not only meets our objectives but also reflects the elegance, usability, and flexibility that Torvel’s design style is renowned for, offering a seamless experience in both light and dark modes.

High end residential end user

```html
<!DOCTYPE html>
<html lang="en">
<head>
<meta charset="utf-8">
<title>Smart Home Control – Dark Mode</title>
<link rel="stylesheet" href="https://fonts.googleapis.com/css2?family=Oswald:wght@500;600;700&family=Poppins:wght@600&display=swap">
<style>
  :root{
    --bg-top:#050468;
    --bg-mid:#28282d;
    --bg-bottom:#403a07;
    --accent-blue:#3f7dff;
    --accent-green:#18f57c;
    --violet-start:#3f4db6;
    --violet-end:#a815ad;
    --divider:#3b57c9;
    --text:#ffffff;
    --hot:#ee2424;
    --cool:#2fb24a;
  }
  *{margin:0;padding:0;box-sizing:border-box}
  html,body{width:1200px;height:616px;overflow:hidden}
  body{
    position:relative;
    background:linear-gradient(180deg,var(--bg-top) 0%,var(--bg-mid) 58%,var(--bg-bottom) 100%);
    font-family:"Oswald",sans-serif;
    color:var(--text);
  }
  .abs{position:absolute}
  .grad-bg{background:linear-gradient(90deg,var(--accent-blue),var(--accent-green))}
  .violet-bg{background:linear-gradient(90deg,var(--violet-start),var(--violet-end))}

  .app-tile{top:32px;width:103px;height:103px;border-radius:20px;display:flex;align-items:center;justify-content:center}
  .app-tile--torvel{left:84px}
  .app-tile--smart{left:201px}
  .torvel-name{font-family:"Oswald",sans-serif;font-weight:600;font-size:24px;color:var(--text)}

  .theme-label{left:948px;top:44px;width:110px;text-align:center;font-size:12px;font-weight:600;font-style:italic}
  .divider{width:3px;background:var(--divider);top:180px;height:179px}

  .btn{display:flex;align-items:center;justify-content:center;font-weight:700;font-style:italic;
       text-shadow:2px 2px 3px rgba(0,0,0,.45);white-space:nowrap;overflow:hidden}
  .btn--tv{left:327px;width:176px;height:50px;font-size:34px}
  .btn--mode{left:927px;width:175px;height:50px;font-size:34px}
  .btn--audio{left:915px;width:176px;height:50px;font-size:34px}

  .heading{font-weight:700;font-style:italic;font-size:34px;line-height:1;white-space:nowrap}
  .heading--temp{left:559px;top:184px;width:336px}
  .heading--streams{left:112px;top:418px}
  .temp-label{font-weight:600;font-style:italic;font-size:37px;line-height:1}
  .temp-rule{left:725px;top:295px;width:175px;height:2px;background:var(--text)}
  .temp-value{left:599px;top:280px;width:92px;text-align:center;font-weight:700;font-style:italic;font-size:37px;line-height:1}

  .stream-rule{left:71px;top:458px;width:788px;height:3px;background:var(--divider)}
  .stream-tile{top:468px;width:94px;height:85px}
  .stream-tile .num{position:absolute;left:5px;top:2px;font-size:11px;font-style:italic;font-weight:500}
  .stream-tile svg{position:absolute;left:40px;top:33px}
</style>
</head>
<body>

<!-- Source tiles -->
<div class="abs app-tile app-tile--torvel grad-bg"><span class="torvel-name">Torvel TV</span></div>
<div class="abs app-tile app-tile--smart grad-bg">
  <svg width="84" height="60" viewBox="0 0 84 60" aria-label="Smart TV">
    <rect x="7" y="3" width="70" height="43" fill="none" stroke="#fff" stroke-width="4"/>
    <text x="42" y="30" fill="#fff" font-family="Poppins,sans-serif" font-weight="600" font-size="12" text-anchor="middle">SMART TV</text>
    <rect x="38" y="46" width="8" height="5" fill="#fff"/>
    <rect x="27" y="51" width="30" height="3" rx="1" fill="#fff"/>
  </svg>
</div>

<!-- Home icon -->
<svg class="abs" style="left:337px;top:32px" width="116" height="104" viewBox="0 0 116 104" aria-label="Home">
  <defs><linearGradient id="homeGrad" x1="0" x2="1"><stop offset="0" stop-color="var(--accent-blue)"/><stop offset="1" stop-color="var(--accent-green)"/></linearGradient></defs>
  <path d="M58 0 L116 50 L96 50 L96 103 L66 103 L66 79 L50 79 L50 103 L20 103 L20 50 L0 50 Z" fill="url(#homeGrad)"/>
</svg>

<!-- Theme toggle -->
<div class="abs theme-label">Theme: Dark Mode</div>
<svg class="abs" style="left:948px;top:63px" width="110" height="49" viewBox="0 0 110 49" aria-label="Theme switch set to dark">
  <defs><linearGradient id="toggleGrad" x1="0" x2="1"><stop offset="0" stop-color="var(--accent-blue)"/><stop offset="1" stop-color="var(--accent-green)"/></linearGradient></defs>
  <rect width="110" height="49" rx="24.5" fill="url(#toggleGrad)"/>
  <circle cx="26" cy="24.5" r="19" fill="#fff"/>
  <circle cx="26" cy="24.5" r="8" fill="#0a0a3a"/>
  <g stroke="#0a0a3a" stroke-width="2">
    <line x1="26" y1="8" x2="26" y2="12"/><line x1="26" y1="37" x2="26" y2="41"/>
    <line x1="9.5" y1="24.5" x2="13.5" y2="24.5"/><line x1="38.5" y1="24.5" x2="42.5" y2="24.5"/>
    <line x1="14" y1="12.5" x2="17" y2="15.5"/><line x1="35" y1="33.5" x2="38" y2="36.5"/>
    <line x1="14" y1="36.5" x2="17" y2="33.5"/><line x1="35" y1="15.5" x2="38" y2="12.5"/>
  </g>
  <circle cx="84" cy="24.5" r="19" fill="#0a0a3a"/>
  <path d="M82 12 A12.5 12.5 0 1 1 82 37 A10 12.5 0 0 0 82 12 Z" fill="#fff"/>
</svg>

<!-- Dividers -->
<div class="abs divider" style="left:41px"></div>
<div class="abs divider" style="left:234px"></div>
<div class="abs divider" style="left:543px"></div>
<div class="abs divider" style="left:913px"></div>

<!-- Directional pad -->
<svg class="abs" style="left:69px;top:196px" width="148" height="148" viewBox="0 0 148 148" aria-label="Directional pad">
  <defs><linearGradient id="padGrad" x1="0" x2="1" y1="0" y2="0.4"><stop offset="0" stop-color="var(--accent-blue)"/><stop offset="1" stop-color="var(--accent-green)"/></linearGradient></defs>
  <circle cx="74" cy="74" r="74" fill="url(#padGrad)"/>
  <g stroke="#2a2340" stroke-width="11">
    <line x1="20" y1="20" x2="128" y2="128"/><line x1="128" y1="20" x2="20" y2="128"/>
  </g>
  <g fill="#fff">
    <polygon points="74,24 84,41 64,41"/><polygon points="74,124 84,107 64,107"/>
    <polygon points="12,74 29,64 29,84"/><polygon points="136,74 119,64 119,84"/>
  </g>
</svg>

<!-- TV control icons -->
<svg class="abs" style="left:257px;top:204px" width="46" height="25" viewBox="0 0 46 25" aria-label="Volume level">
  <defs><linearGradient id="iconGrad" x1="0" x2="1"><stop offset="0" stop-color="var(--accent-blue)"/><stop offset="1" stop-color="var(--accent-green)"/></linearGradient></defs>
  <rect x="0" y="15" width="10" height="10" fill="url(#iconGrad)"/><rect x="12" y="10" width="10" height="15" fill="url(#iconGrad)"/>
  <rect x="24" y="5" width="10" height="20" fill="url(#iconGrad)"/><rect x="36" y="0" width="10" height="25" fill="url(#iconGrad)"/>
</svg>
<svg class="abs" style="left:257px;top:255px" width="45" height="29" viewBox="0 0 45 29" aria-label="Channel grid">
  <defs><linearGradient id="gridGrad" x1="0" x2="1"><stop offset="0" stop-color="var(--accent-blue)"/><stop offset="1" stop-color="var(--accent-green)"/></linearGradient></defs>
  <g fill="url(#gridGrad)">
    <rect x="0" y="0" width="13" height="12"/><rect x="16" y="0" width="13" height="12"/><rect x="32" y="0" width="13" height="12"/>
    <rect x="0" y="16" width="13" height="13"/><rect x="16" y="16" width="13" height="13"/><rect x="32" y="16" width="13" height="13"/>
  </g>
</svg>
<svg class="abs" style="left:262px;top:313px" width="41" height="38" viewBox="0 0 41 38" aria-label="Menu list">
  <defs><linearGradient id="menuGrad" x1="0" x2="1"><stop offset="0" stop-color="var(--accent-blue)"/><stop offset="1" stop-color="var(--accent-green)"/></linearGradient></defs>
  <rect width="41" height="38" fill="url(#menuGrad)"/>
  <g stroke="#14163a" stroke-width="1.5"><line x1="5" y1="8" x2="36" y2="8"/><line x1="5" y1="15" x2="36" y2="15"/><line x1="5" y1="22" x2="36" y2="22"/><line x1="5" y1="29" x2="36" y2="29"/></g>
</svg>

<!-- TV buttons -->
<div class="abs btn btn--tv violet-bg" style="top:180px">VOLUME</div>
<div class="abs btn btn--tv violet-bg" style="top:242px">CHANNEL</div>
<div class="abs btn btn--tv violet-bg" style="top:309px">MENU</div>

<!-- Temperature control -->
<div class="abs heading heading--temp">TEMPERATURE CONTROL</div>
<svg class="abs" style="left:580px;top:239px" width="130" height="130" viewBox="0 0 130 130" aria-label="Thermostat dial">
  <defs>
    <linearGradient id="ringGrad" x1="0" x2="1"><stop offset="0" stop-color="var(--cool)"/><stop offset="0.5" stop-color="#9a7a3a"/><stop offset="1" stop-color="var(--hot)"/></linearGradient>
  </defs>
  <circle cx="65" cy="65" r="61" fill="none" stroke="url(#ringGrad)" stroke-width="4"/>
  <circle cx="65" cy="65" r="46" fill="url(#ringGrad)"/>
</svg>
<div class="abs temp-value">23°C</div>
<div class="abs temp-label" style="left:729px;top:250px">Max.</div>
<div class="abs temp-rule"></div>
<div class="abs temp-label" style="left:729px;top:302px">Min.</div>

<!-- HVAC modes -->
<div class="abs btn btn--mode grad-bg" style="top:170px">NORMAL</div>
<div class="abs btn btn--mode grad-bg" style="top:243px">ECO</div>
<div class="abs btn btn--mode grad-bg" style="top:322px">OFF</div>

<!-- Camera streams -->
<div class="abs heading heading--streams">CAMERA STREAMS</div>
<div class="abs stream-rule"></div>
<div class="abs stream-tile violet-bg" style="left:71px"><span class="num">01</span><svg width="16" height="18"><polygon points="0,0 16,9 0,18" fill="#fff"/></svg></div>
<div class="abs stream-tile violet-bg" style="left:184px"><span class="num">02</span><svg width="16" height="18"><polygon points="0,0 16,9 0,18" fill="#fff"/></svg></div>
<div class="abs stream-tile violet-bg" style="left:296px"><span class="num">03</span><svg width="16" height="18"><polygon points="0,0 16,9 0,18" fill="#fff"/></svg></div>
<div class="abs stream-tile violet-bg" style="left:409px"><span class="num">04</span><svg width="16" height="18"><polygon points="0,0 16,9 0,18" fill="#fff"/></svg></div>
<div class="abs stream-tile violet-bg" style="left:522px"><span class="num">05</span><svg width="16" height="18"><polygon points="0,0 16,9 0,18" fill="#fff"/></svg></div>
<div class="abs stream-tile violet-bg" style="left:637px"><span class="num">05</span><svg width="16" height="18"><polygon points="0,0 16,9 0,18" fill="#fff"/></svg></div>
<div class="abs stream-tile violet-bg" style="left:751px"><span class="num">05</span><svg width="16" height="18"><polygon points="0,0 16,9 0,18" fill="#fff"/></svg></div>

<!-- Audio -->
<div class="abs btn btn--audio grad-bg" style="top:442px">AUDIO on</div>
<div class="abs btn btn--audio grad-bg" style="top:516px">MUTE</div>
<svg class="abs" style="left:1110px;top:447px" width="52" height="42" viewBox="0 0 52 42" aria-label="Speaker on">
  <path d="M0 14 H10 L24 3 V39 L10 28 H0 Z" fill="var(--divider)"/>
  <g fill="none" stroke="var(--divider)" stroke-width="3" stroke-linecap="round">
    <path d="M30 14 Q34 21 30 28"/><path d="M36 9 Q42 21 36 33"/><path d="M42 4 Q50 21 42 38"/>
  </g>
</svg>
<svg class="abs" style="left:1110px;top:520px" width="60" height="44" viewBox="0 0 60 44" aria-label="Speaker muted">
  <path d="M0 15 H10 L24 4 V40 L10 29 H0 Z" fill="var(--divider)"/>
  <g fill="none" stroke="var(--divider)" stroke-width="3" stroke-linecap="round">
    <path d="M30 15 Q34 22 30 29"/><path d="M36 10 Q42 22 36 34"/><path d="M42 5 Q50 22 42 39"/>
  </g>
  <line x1="8" y1="42" x2="58" y2="2" stroke="#1b1b3a" stroke-width="3"/>
</svg>

</body>
</html>
```